Small Business Consulting Firm Needs Business Card Design

Need a sleek modern business card with 2 sides matching the colors of our logo. We will be placing these with a mailer we are sending out. These business cards will only ever be given to business owners. We operate helping businesses who are struggling with cash flow or finances. If the green and blue design needs to be moved to the right of "Harborline Crest Consulting" for aesthetic purposes that is ok. We will need an editable file if possible. We would like to include the reps name, email, website, and phone number. For now just use Peter Vance, pvance@harborlinecrest.com, www.harborlinecrest.com, and 833-555-0172.

```html
<!DOCTYPE html>
<html lang="en">
<head>
<meta charset="utf-8">
<title>Harborline Crest Consulting – Business Card</title>
<link href="https://fonts.googleapis.com/css2?family=Lato:wght@300;400;700;900&display=swap" rel="stylesheet">
<style>
  :root {
    --page: #2e2e2e;
    --card: #ffffff;
    --green: #6cb33f;
    --green-deep: #4f9a3a;
    --blue: #0a6ab8;
    --blue-deep: #0b4f9e;
    --ink: #3a3a3a;
    --ink-soft: #555555;
  }
  * { box-sizing: border-box; margin: 0; padding: 0; }
  html, body {
    width: 1200px; height: 866px; overflow: hidden;
    background: var(--page);
    font-family: "Lato", Arial, sans-serif;
  }
  .sheet {
    width: 1200px; height: 866px;
    display: flex; align-items: center; justify-content: center; gap: 40px;
  }
  .card {
    position: relative;
    width: 545px; height: 311px;
    overflow: hidden;
    box-shadow: 0 10px 24px rgba(0,0,0,.45);
  }

  /* Front */
  .card--front { background: var(--card); }
  .rep {
    position: absolute; left: 36px; top: 104px;
  }
  .rep__name {
    font-weight: 900; font-size: 21px; letter-spacing: .5px;
    text-transform: uppercase; margin-bottom: 12px;
  }
  .rep__first { color: var(--green); }
  .rep__last { color: var(--blue); }
  .contact { list-style: none; }
  .contact__item {
    display: flex; align-items: center; gap: 8px;
    font-size: 13.5px; color: var(--ink-soft); line-height: 20px;
  }
  .contact__icon { width: 12px; height: 12px; flex: none; }

  .brand {
    position: absolute; right: 34px; top: 128px;
    display: flex; flex-direction: column; align-items: flex-start;
  }
  .brand__mark {
    width: 46px; height: 46px; background: var(--green);
    align-self: flex-end; margin: 0 22px 14px 0;
  }
  .brand__name {
    color: var(--ink); font-weight: 400;
    font-size: 25px; letter-spacing: 3px; text-transform: uppercase; line-height: 1;
  }
  .brand__tag {
    color: var(--ink); font-weight: 400;
    font-size: 10px; letter-spacing: 7.5px; text-transform: uppercase;
    margin: 6px 0 0 30px;
  }
  .stripe {
    position: absolute; left: 0; right: 0; bottom: 0; height: 9px;
    display: flex;
  }
  .stripe__blue { width: 45%; background: var(--blue); }
  .stripe__green { flex: 1; background: var(--green); }

  /* Back */
  .card--back {
    background: linear-gradient(120deg, var(--blue-deep) 0%, #146e8a 45%, var(--green-deep) 80%, var(--green) 100%);
    display: flex; flex-direction: column; align-items: center; justify-content: center;
  }
  .card--back .brand__name { color: #ffffff; font-size: 26px; }
  .card--back .brand__tag { color: #ffffff; margin-left: 0; align-self: center; }
</style>
</head>
<body>
<main class="sheet">
  <section class="card card--front" aria-label="Card front">
    <div class="rep">
      <h1 class="rep__name"><span class="rep__first">Peter</span> <span class="rep__last">Vance</span></h1>
      <ul class="contact">
        <li class="contact__item">
          <svg class="contact__icon" viewBox="0 0 12 12"><path fill="#6cb33f" d="M1 4c0-1 1-2 2-2h6c1 0 2 1 2 2v1H8.5V4h-5v1H1zM2 6h8l1 5H1z"/><circle cx="6" cy="8.3" r="1.3" fill="#fff"/></svg>
          833-555-0172
        </li>
        <li class="contact__item">
          <svg class="contact__icon" viewBox="0 0 12 12"><rect x="0.5" y="2" width="11" height="8" fill="#6cb33f"/><path d="M0.8 2.4 6 6.6l5.2-4.2" fill="none" stroke="#fff" stroke-width="1"/></svg>
          pvance@harborlinecrest.com
        </li>
        <li class="contact__item">
          <svg class="contact__icon" viewBox="0 0 12 12"><circle cx="6" cy="6" r="5.5" fill="#6cb33f"/><path d="M0.5 6h11M6 .5c2 2 2 9 0 11M6 .5c-2 2-2 9 0 11" fill="none" stroke="#fff" stroke-width=".8"/></svg>
          www.harborlinecrest.com
        </li>
      </ul>
    </div>
    <div class="brand">
      <span class="brand__mark" aria-hidden="true"></span>
      <p class="brand__name">Harborline Crest</p>
      <p class="brand__tag">Consulting</p>
    </div>
    <div class="stripe" aria-hidden="true">
      <span class="stripe__blue"></span><span class="stripe__green"></span>
    </div>
  </section>

  <section class="card card--back" role="img" aria-label="Card back: blue to green faceted gradient with company name">
    <p class="brand__name">Harborline Crest</p>
    <p class="brand__tag">Consulting</p>
  </section>
</main>
</body>
</html>
```